CareRally482
Business Cards and Stationary
CareRally482 - Emergency Services
Creative Brief
Use specific fonts
Use fonts and colors from our new logo and website that are attached
Professional
Gordon P. Hartwell
Owner
20415 E Ridge Ave Suite 230-519 Surprise, AZ 85261
gph@carerally482.com
www.carerally482.com
Use uploaded website draft for colors and fonts, you can get an idea of what we do from the current website. NOTE: We will need business card templates for; Marlena J. Hartwell Owner cell (623) 555-0187 email marlena@carerally482.com Douglas R. Pembry DO Medical Director cell (602)555-0134 email dpembrydo@carerally482.com
open to great ideas

```html
<!DOCTYPE html>
<html lang="en">
<head>
<meta charset="utf-8">
<title>CareRally482 Stationery</title>
<link href="https://fonts.googleapis.com/css2?family=Open+Sans:wght@400;600;800&display=swap" rel="stylesheet">
<style>
:root{
  --bg:#8f9398;
  --paper:#ffffff;
  --blue:#1d56b8;
  --blue-dark:#0c2f7c;
  --blue-light:#4f86d8;
  --ink:#3a3f48;
  --rule:#b9bec6;
  --faint:#e9eef7;
}
*{box-sizing:border-box;margin:0;padding:0}
html,body{width:1200px;height:648px;overflow:hidden;background:var(--bg);font-family:"Open Sans",sans-serif;color:var(--ink)}
.canvas{position:relative;width:1200px;height:648px}
.sheet{position:absolute;background:var(--paper);box-shadow:0 2px 4px rgba(0,0,0,.25);overflow:hidden}
.brand{font-weight:800;color:var(--blue-dark);letter-spacing:.5px;display:flex;align-items:center;gap:4px;white-space:nowrap}
.brand .dot{display:inline-block;border-radius:50%;background:var(--blue)}
.contact{position:absolute;font-size:4.5px;line-height:6px;color:var(--ink);white-space:nowrap}
.decor-area{position:absolute;background:radial-gradient(ellipse at center,var(--faint) 0%,rgba(233,238,247,.6) 45%,rgba(255,255,255,0) 72%)}
.footer-band{position:absolute;left:0;right:0;bottom:0;height:14px;background:linear-gradient(90deg,var(--blue-dark),var(--blue) 60%,var(--blue-light))}

/* letterheads */
.letterhead{top:139px;width:344px;height:499px}
.letterhead.fax{left:19px}
.letterhead.plain{left:391px}
.letterhead .brand{position:absolute;left:22px;top:20px;font-size:12px}
.letterhead .brand .dot{width:14px;height:14px}
.letterhead .contact{left:236px;top:16px}
.letterhead .decor-area{left:50px;top:310px;width:280px;height:175px}
.fax-title{position:absolute;right:22px;top:58px;font-size:8px;font-weight:800;color:var(--ink)}
.fax-table{position:absolute;left:22px;top:70px;width:300px;border-collapse:collapse;font-size:5px}
.fax-table td{border:1px solid var(--rule);height:16px;padding:0 4px;width:25%}
.fax-table td.label{background:#f1f3f6;font-weight:600}
.fax-checks{position:absolute;left:22px;top:144px;width:300px;display:flex;justify-content:space-between;font-size:5px}
.fax-checks span{display:flex;align-items:center;gap:3px}
.fax-checks i{display:inline-block;width:6px;height:6px;border:1px solid var(--ink)}

/* cards */
.card{width:161px;height:77px;border-radius:3px}
.card.front{top:24px;background:linear-gradient(180deg,#fff 0 80%,var(--faint))}
.card.front .top-band{position:absolute;left:0;right:0;top:0;height:5px;background:var(--blue)}
.card.front .brand{position:absolute;left:8px;top:10px;font-size:8px}
.card.front .brand .dot{width:9px;height:9px}
.card.front .contact{left:8px;top:26px;font-size:4px;line-height:5.2px}
.card.front .contact b{font-size:5px;color:var(--blue-dark)}
.card.front .portrait{position:absolute;right:10px;top:14px;width:44px;height:50px;background:linear-gradient(180deg,#c9ccd3,#5a6272)}
.card.front .bottom-band{position:absolute;left:0;right:0;bottom:0;height:8px;background:linear-gradient(90deg,var(--blue-dark),var(--blue-light))}
.card.back{top:120px;background:radial-gradient(ellipse at 60% 40%,var(--blue-light),var(--blue) 45%,var(--blue-dark))}
.card.c1{left:768px}
.card.c2{left:938px}

/* envelopes */
.envelope{left:768px;width:331px}
.envelope.front{top:233px;height:206px}
.envelope.front .brand{position:absolute;left:14px;top:14px;font-size:11px}
.envelope.front .brand .dot{width:12px;height:12px}
.envelope.front .contact{left:14px;top:150px}
.envelope.front .decor-area{left:80px;top:45px;width:240px;height:140px}
.envelope.front .footer-band{height:10px}
.envelope.back{top:456px;height:163px}
.envelope.back .flap{position:absolute;left:0;top:0}
.envelope.back .band{position:absolute;left:0;right:0;top:40px;height:44px;background:linear-gradient(90deg,var(--blue-dark),var(--blue) 55%,var(--blue-light));display:flex;align-items:center;justify-content:center}
.envelope.back .brand{color:#fff;font-size:11px}
.envelope.back .brand .dot{width:12px;height:12px;background:#fff}
</style>
</head>
<body>
<div class="canvas">

  <section class="sheet letterhead fax">
    <div class="brand">CareRally482 <span class="dot"></span></div>
    <div class="contact">20415 E Ridge Ave Suite 230-519<br>Surprise, AZ 85261<br>(623) 555-0187<br>gph@carerally482.com<br>www.carerally482.com</div>
    <div class="fax-title">FAX</div>
    <table class="fax-table">
      <tr><td class="label">To:</td><td></td><td class="label">From:</td><td></td></tr>
      <tr><td class="label">Fax:</td><td></td><td class="label">Pages:</td><td></td></tr>
      <tr><td class="label">Phone:</td><td></td><td class="label">Date:</td><td></td></tr>
      <tr><td class="label">Re:</td><td></td><td class="label">CC:</td><td></td></tr>
    </table>
    <div class="fax-checks">
      <span><i></i>Urgent</span><span><i></i>For Review</span><span><i></i>Please Comment</span><span><i></i>Please Reply</span><span><i></i>Please Recycle</span>
    </div>
    <div class="decor-area" role="img" aria-label="Faint decorative brand graphic"></div>
    <div class="footer-band"></div>
  </section>

  <section class="sheet letterhead plain">
    <div class="brand">CareRally482 <span class="dot"></span></div>
    <div class="contact">20415 E Ridge Ave Suite 230-519<br>Surprise, AZ 85261<br>(623) 555-0187<br>gph@carerally482.com<br>www.carerally482.com</div>
    <div class="decor-area" role="img" aria-label="Faint decorative brand graphic"></div>
    <div class="footer-band"></div>
  </section>

  <section class="sheet card front c1">
    <div class="top-band"></div>
    <div class="brand">CareRally482 <span class="dot"></span></div>
    <div class="contact"><b>Gordon P. Hartwell</b><br>Owner<br>20415 E Ridge Ave Suite 230-519<br>Surprise, AZ 85261<br>gph@carerally482.com<br>www.carerally482.com</div>
    <div class="portrait" role="img" aria-label="Portrait photo of Gordon P. Hartwell"></div>
    <div class="bottom-band"></div>
  </section>

  <section class="sheet card front c2">
    <div class="top-band"></div>
    <div class="brand">CareRally482 <span class="dot"></span></div>
    <div class="contact"><b>Marlena J. Hartwell</b><br>Owner<br>cell (623) 555-0187<br>marlena@carerally482.com<br>www.carerally482.com</div>
    <div class="portrait" role="img" aria-label="Portrait photo of Marlena J. Hartwell"></div>
    <div class="bottom-band"></div>
  </section>

  <section class="sheet card back c1" role="img" aria-label="Blue card back with decorative brand graphic"></section>
  <section class="sheet card back c2" role="img" aria-label="Blue card back with decorative brand graphic"></section>

  <section class="sheet envelope front">
    <div class="brand">CareRally482 <span class="dot"></span></div>
    <div class="decor-area" role="img" aria-label="Faint decorative brand graphic"></div>
    <div class="contact">20415 E Ridge Ave Suite 230-519<br>Surprise, AZ 85261<br>(623) 555-0187<br>www.carerally482.com</div>
    <div class="footer-band"></div>
  </section>

  <section class="sheet envelope back">
    <svg class="flap" width="331" height="163" viewBox="0 0 331 163" aria-hidden="true">
      <path d="M0 0 L165 84 L331 0" fill="none" stroke="var(--rule)" stroke-width="1"/>
    </svg>
    <div class="band"><div class="brand">CareRally482 <span class="dot"></span></div></div>
  </section>

</div>
</body>
</html>
```